Modern Business Card for Lanternfield 2018

Our company assumes the best about people. We are creating an online community of entrepreneurs and business leaders who struggle with marketing their business online.

This business card should POP! We recently got a new logo and are launching a new website next month, so our business cards should make a statement that feels:
-Fresh
-Smart
-Trustworthy
-Fun

Target Market(s)

small business owners, entrepreneurs

Industry/Entity Type

Digital Marketing

Contact Information for Business Card

Dimensions: 3.5" x 2"

Font styles to use
Sans Serif

Colors
f37122
ffffff

Requirements
Must have
• We need a business card with a modern, bold design. We will use one side of the card as a lead-generation offer, so text on one side will need to fit up to 140 characters. The business card should stick to our core colors (orange, black, and white).
Nice to have
• We think a vertical "portrait" design could be interesting.
Should not have
• Should not look like a traditional business card. The round icon should stand out from a distance.

```html
<!DOCTYPE html>
<html lang="en">
<head>
<meta charset="UTF-8">
<title>Lanternfield Business Card</title>
<link href="https://fonts.googleapis.com/css2?family=Montserrat:wght@400;500;700;800&display=swap" rel="stylesheet">
<style>
  :root {
    --orange: #f37122;
    --white: #ffffff;
    --black: #1a1a1a;
    --backdrop: #e9e6e1;
    --silver-light: #f4f4f4;
    --silver-dark: #c9c9c9;
    --rule: #8a8a8a;
  }
  * { box-sizing: border-box; margin: 0; padding: 0; }
  html, body {
    width: 1200px; height: 911px; overflow: hidden;
    background: var(--backdrop);
    font-family: "Montserrat", sans-serif;
  }
  .sheet {
    width: 1200px; height: 911px;
    display: flex; justify-content: center; align-items: center; gap: 90px;
  }
  .card {
    width: 360px; height: 630px;
    position: relative; overflow: hidden;
    box-shadow: 0 14px 30px rgba(0,0,0,.18);
  }

  /* Front */
  .card-front { background: var(--white); }
  .contact-cap {
    position: absolute; left: -50px; top: -180px;
    width: 460px; height: 400px;
    border-radius: 50%;
    background: var(--orange);
  }
  .contact {
    position: absolute; top: 42px; left: 0; width: 100%;
    text-align: center; color: var(--white); text-transform: uppercase;
  }
  .contact-name { font-weight: 800; font-size: 27px; letter-spacing: .5px; }
  .contact-title { font-weight: 700; font-size: 17px; margin-top: 4px; letter-spacing: .5px; }
  .contact-email { font-weight: 400; font-size: 14.5px; margin-top: 5px; letter-spacing: .3px; }
  .brand {
    position: absolute; top: 360px; left: 0; width: 100%;
    text-align: center;
  }
  .brand-dot {
    width: 34px; height: 34px; border-radius: 50%;
    background: var(--orange); margin: 0 auto 10px;
  }
  .brand-name {
    font-weight: 800; font-size: 38px; color: var(--black); letter-spacing: 1px;
  }
  .brand-tagline {
    font-weight: 500; font-size: 11.5px; color: var(--black);
    text-transform: uppercase; letter-spacing: 2px; margin-top: 6px;
  }

  /* Back */
  .card-back { background: var(--orange); color: var(--white); }
  .offer-headline {
    position: absolute; top: 40px; left: 0; width: 100%;
    text-align: center; text-transform: uppercase;
    font-weight: 800; font-size: 25px; line-height: 1.15; letter-spacing: .5px;
  }
  .offer-mark {
    position: absolute; top: 160px; left: 50%;
    width: 120px; height: 120px; margin-left: -60px;
    border-radius: 50%; background: var(--white);
  }
  .offer-copy {
    position: absolute; top: 304px; left: 30px; right: 30px;
    text-align: center; text-transform: uppercase;
    font-weight: 400; font-size: 17px; line-height: 1.25;
  }
  .offer-copy strong { font-weight: 800; }
  .offer-link {
    position: absolute; top: 386px; left: 42px; right: 42px;
    height: 34px; border-radius: 17px;
    background: var(--black); color: var(--orange);
    font-weight: 700; font-size: 16px;
    display: flex; align-items: center; justify-content: center;
    z-index: 2;
  }
  .notes {
    position: absolute; top: 408px; left: 22px; right: 22px; height: 196px;
    border-radius: 14px;
    background: linear-gradient(100deg, var(--silver-dark), var(--silver-light) 45%, var(--silver-dark));
    padding: 30px 22px 0;
  }
  .notes-line {
    border-bottom: 1.5px dotted var(--rule);
    height: 23px;
  }
</style>
</head>
<body>
<main class="sheet">
  <section class="card card-front">
    <div class="contact-cap"></div>
    <div class="contact">
      <p class="contact-name">Dana Whitlow</p>
      <p class="contact-title">Story Marketing Coach</p>
      <p class="contact-email">dana@lanternfieldhq.com</p>
    </div>
    <div class="brand">
      <div class="brand-dot"></div>
      <p class="brand-name">LANTERNFIELD</p>
      <p class="brand-tagline">Tell stories that inspire action</p>
    </div>
  </section>

  <section class="card card-back">
    <h2 class="offer-headline">Reach more people.<br>Make more money.<br>Create more impact.</h2>
    <div class="offer-mark"></div>
    <p class="offer-copy">Get your free <strong>Lanternfield</strong> starter package and our marketing guide today at</p>
    <div class="offer-link">Lanternfieldhq.com/start</div>
    <div class="notes">
      <div class="notes-line"></div>
      <div class="notes-line"></div>
      <div class="notes-line"></div>
      <div class="notes-line"></div>
      <div class="notes-line"></div>
      <div class="notes-line"></div>
      <div class="notes-line"></div>
    </div>
  </section>
</main>
</body>
</html>
```